Plastic Pots, Hanging Baskets, and Plastic Tray Manufacturer Catalog

Catalog design for a newer company looking for a fresh take on plastics offerings, need layout design but attached some ideas in the project

Industry/Entity Type

It Company

Colors
a2cd3a
cadf82
eaf2ce

```html
<!DOCTYPE html>
<html lang="en">
<head>
<meta charset="utf-8">
<title>Verdell Plastics Catalog Cover</title>
<link rel="stylesheet" href="https://fonts.googleapis.com/css2?family=Montserrat:wght@400;600;700&display=swap">
<style>
  :root {
    --backdrop: #d9d6d0;
    --page: #151515;
    --page-light: #222222;
    --facet: #1c1c1c;
    --brand-green: #a2cd3a;
    --brand-mid: #cadf82;
    --brand-pale: #eaf2ce;
    --text-soft: #9a9a9a;
    --text-head: #b8b8b8;
  }
  html, body {
    margin: 0;
    padding: 0;
    width: 1200px;
    height: 584px;
    overflow: hidden;
    background: var(--backdrop);
    font-family: "Montserrat", sans-serif;
  }
  .spread {
    position: absolute;
    left: 20px;
    top: 78px;
    width: 1158px;
    height: 418px;
    display: flex;
  }
  .page {
    position: relative;
    width: 50%;
    height: 100%;
    background: var(--page);
    overflow: hidden;
  }
  .page + .page { border-left: 1px solid #2c2c2c; }
  .facets {
    position: absolute;
    inset: 0;
    width: 100%;
    height: 100%;
  }
  .brand {
    position: absolute;
    display: flex;
    align-items: center;
    gap: 8px;
    color: var(--text-head);
    font-weight: 600;
    white-space: nowrap;
  }
  .brand-dot {
    border-radius: 50%;
    background: var(--brand-green);
    flex: none;
  }
  .brand--back { left: 65px; top: 200px; flex-direction: column; align-items: flex-start; font-size: 12px; }
  .brand--back .brand-dot { width: 44px; height: 44px; margin-left: 24px; }
  .brand--front { right: 16px; top: 26px; font-size: 20px; }
  .brand--front .brand-dot { width: 34px; height: 34px; }
  .contact {
    position: absolute;
    left: 65px;
    top: 284px;
    color: var(--text-soft);
  }
  .contact-title {
    margin: 0 0 6px;
    font-size: 12px;
    font-weight: 700;
    letter-spacing: 0.06em;
    color: var(--text-head);
  }
  .contact-list { list-style: none; margin: 0; padding: 0; font-size: 7.5px; line-height: 10.6px; }
  .contact-list li { display: flex; gap: 5px; }
  .contact-list svg { flex: none; margin-top: 2px; }
  .photo-strip {
    position: absolute;
    left: 0;
    right: 0;
    top: 279px;
    height: 109px;
    display: flex;
    gap: 4px;
  }
  .photo { height: 100%; }
  .photo--hands { flex: 203; background: linear-gradient(135deg, #6f8f52, #b98a5c 55%, #c9c2b0); }
  .photo--seedlings { flex: 198; background: linear-gradient(135deg, #5e8a3e, #9fb56a 45%, #c79a6a 75%, #3b5f8a); }
  .photo--tray { flex: 172; background: linear-gradient(135deg, #d7dde0, #9a8c70 55%, #3a3022); }
  .base-band {
    position: absolute;
    left: 0; right: 0; bottom: 0;
    height: 30px;
    background: #101010;
  }
</style>
</head>
<body>
<main class="spread">
  <section class="page page--back">
    <svg class="facets" viewBox="0 0 579 418" preserveAspectRatio="none" aria-hidden="true">
      <polygon points="0,0 579,0 579,418" fill="var(--facet)"/>
      <polygon points="0,0 290,210 0,418" fill="var(--page-light)" opacity="0.5"/>
      <polygon points="290,210 579,0 579,418" fill="#0f0f0f" opacity="0.6"/>
    </svg>
    <div class="brand brand--back">
      <span class="brand-dot"></span>
      <span class="brand-name">Verdell Plastics</span>
    </div>
    <div class="contact">
      <h2 class="contact-title">CONTACT US</h2>
      <ul class="contact-list">
        <li><svg width="6" height="7" viewBox="0 0 6 7"><path d="M3 0a2.4 2.4 0 0 0-2.4 2.4C.6 4.2 3 7 3 7s2.4-2.8 2.4-4.6A2.4 2.4 0 0 0 3 0z" fill="currentColor"/></svg><span>1450 W. Meadow Ave, Suite<br>210, Fresno, CA 93711</span></li>
        <li><svg width="6" height="6" viewBox="0 0 6 6"><path d="M1 0l1.3 1.5-.7 1c.5 1 1 1.5 1.9 1.9l1-.7L6 5 5 6C2.5 5.6.4 3.5 0 1z" fill="currentColor"/></svg><span>(555)014 2200</span></li>
        <li><svg width="6" height="6" viewBox="0 0 6 6"><rect x="0" y="1" width="6" height="4" rx="0.5" fill="currentColor"/></svg><span>(555)014 2201</span></li>
        <li><svg width="6" height="6" viewBox="0 0 6 6"><circle cx="3" cy="3" r="2.5" fill="none" stroke="currentColor"/></svg><span>info@verdellplastics.com</span></li>
        <li><svg width="6" height="6" viewBox="0 0 6 6"><circle cx="3" cy="3" r="2.5" fill="currentColor"/></svg><span>www.verdellplastics.com</span></li>
      </ul>
    </div>
  </section>
  <section class="page page--front">
    <svg class="facets" viewBox="0 0 579 418" preserveAspectRatio="none" aria-hidden="true">
      <polygon points="0,0 290,210 579,0" fill="var(--facet)"/>
      <polygon points="0,0 290,210 0,418" fill="#101010" opacity="0.7"/>
      <polygon points="579,0 290,210 579,418" fill="var(--page-light)" opacity="0.5"/>
    </svg>
    <div class="brand brand--front">
      <span class="brand-dot"></span>
      <span class="brand-name">Verdell Plastics</span>
    </div>
    <div class="photo-strip">
      <div class="photo photo--hands" role="img" aria-label="Photo: hands planting a seedling into small plastic and clay pots on a workbench"></div>
      <div class="photo photo--seedlings" role="img" aria-label="Photo: young plants in plastic nursery pots beside a wooden crate"></div>
      <div class="photo photo--tray" role="img" aria-label="Photo: black square plastic pot with a flower set on a sandy shore"></div>
    </div>
    <div class="base-band"></div>
  </section>
</main>
</body>
</html>
```